Telecommunications/Power civil contractor needs business card design

Were a new telecommunications/power underground civil contractor that is looking for a new business card design. Our company colours are silver or grey and orange. Feel free to use the white background logo or the black background logo.

Target Market(s)

Local contractors, utility companies, private sector mining/energy companies, developers.

Industry/Entity Type

Telecommunications

Contact Information for Business Card

Each card will need the following info:
Persons name:
Title:
E-mail:
Phone number:
Shop Address:
Mailing Address:

Requirements
Must have
• Each card will need the following info:
• Persons name:
• Title:
• E-mail:
• Phone number:
• Shop Address:
• Mailing Address:

```html
<!DOCTYPE html>
<html lang="en">
<head>
<meta charset="UTF-8">
<title>Tarrow Civil Contracting Inc – Business Card</title>
<link rel="stylesheet" href="https://fonts.googleapis.com/css2?family=Lato:ital,wght@0,300;0,400;0,700;1,400&display=swap">
<style>
  :root {
    --page-bg: #d6d9dc;
    --card-bg: #eff0f1;
    --card-edge: #c4c7ca;
    --band: #111111;
    --accent: #d0391a;
    --name-red: #b3321b;
    --ink: #2b2b2b;
    --logo-grey: #3a3b3d;
    --band-text: #f2f2f2;
  }
  * { margin: 0; padding: 0; box-sizing: border-box; }
  html, body {
    width: 1200px; height: 970px; overflow: hidden;
    background: var(--page-bg);
    font-family: "Lato", sans-serif;
  }
  .card {
    position: absolute; left: 100px; top: 185px;
    width: 1000px; height: 600px;
    background: var(--card-bg);
    border: 1px solid var(--card-edge);
  }
  .brand {
    position: absolute; left: 200px; top: 70px;
    display: flex; align-items: center; gap: 36px;
  }
  .brand-dot {
    width: 120px; height: 120px; border-radius: 50%;
    background: var(--accent);
  }
  .brand-name {
    font-weight: 700; color: var(--logo-grey);
    text-transform: uppercase; line-height: 1.05;
  }
  .brand-name .line-main { display: block; font-size: 54px; letter-spacing: 2px; }
  .brand-name .line-sub { display: block; font-size: 30px; letter-spacing: 3px; }
  .name-band {
    position: absolute; left: 0; top: 282px;
    width: 100%; height: 91px;
    background: var(--band);
    display: flex; align-items: center;
  }
  .person-name {
    width: 486px; text-align: right; padding-right: 16px;
    color: var(--name-red); font-weight: 700; font-size: 30px;
    border-right: 1px solid var(--name-red);
    line-height: 58px;
  }
  .person-title {
    padding-left: 16px; color: var(--band-text);
    font-weight: 400; font-size: 25px;
  }
  .contact {
    position: absolute; left: 0; top: 425px; width: 100%;
    display: flex; flex-direction: column; align-items: center; gap: 14px;
    font-size: 23px; color: var(--ink);
  }
  .contact-row { display: flex; align-items: center; gap: 44px; }
  .contact-item { display: flex; align-items: center; gap: 8px; }
  .contact-item svg { fill: var(--accent); flex: none; }
  .addr-tag { color: var(--accent); font-style: italic; margin-left: 6px; }
</style>
</head>
<body>
  <main class="card">
    <div class="brand">
      <div class="brand-dot"></div>
      <div class="brand-name">
        <span class="line-main">Tarrow Civil</span>
        <span class="line-sub">Contracting Inc</span>
      </div>
    </div>

    <div class="name-band">
      <div class="person-name">Daniel Carver</div>
      <div class="person-title">Chief Operating Officer</div>
    </div>

    <div class="contact">
      <div class="contact-row">
        <span class="contact-item">
          <svg width="24" height="20" viewBox="0 0 24 20" aria-hidden="true"><path d="M2 6c0-3 4-5 10-5s10 2 10 5v2h-6V6H8v2H2z"/><path d="M5 9h14l2 10H3z"/><circle cx="12" cy="14" r="3" fill="#eff0f1"/></svg>
          412-555-0148
        </span>
        <span class="contact-item">
          <svg width="24" height="18" viewBox="0 0 24 18" aria-hidden="true"><rect x="0" y="0" width="24" height="18" rx="1"/><path d="M1 1l11 9 11-9" fill="none" stroke="#eff0f1" stroke-width="2"/></svg>
          enquiries@tarrowcivil.com
        </span>
      </div>
      <div class="contact-item">
        <svg width="18" height="24" viewBox="0 0 18 24" aria-hidden="true"><path d="M9 0a9 9 0 0 0-9 9c0 6 9 15 9 15s9-9 9-15a9 9 0 0 0-9-9z"/><circle cx="9" cy="9" r="3.5" fill="#eff0f1"/></svg>
        84 Harlow Drive, Brookfield, PA 15210<span class="addr-tag">(Shop)</span>
      </div>
      <div class="contact-item">
        <svg width="18" height="24" viewBox="0 0 18 24" aria-hidden="true"><path d="M9 0a9 9 0 0 0-9 9c0 6 9 15 9 15s9-9 9-15a9 9 0 0 0-9-9z"/><circle cx="9" cy="9" r="3.5" fill="#eff0f1"/></svg>
        #1420 Linden Avenue, Fairmont, New York<span class="addr-tag">(Mailing)</span>
      </div>
    </div>
  </main>
</body>
</html>
```